Create Design/GRAPHICS/TEXT FOR CORVELLE/E-COMMERCE PRODUCT

Hi,
I am looking for a designer to create a advertisement/images/text for a product that I sell on Corvelle.
The first attachment is a 3d rendering of the product that I sell and want to use as the main image of the design.
The second attachment is of a existing ad on Corvelle that you can use as a general idea of how I want the final graphic to look like.
The third and fourth attachments are of the text/graphics that I would like for you to include in the graphic.
Finally, the last attachment is my logo that I would like to include in the graphic.
Please feel free to get creative with this and if you have any questions please feel free to contact me.-
Update-I just added source files for logo as attachment six.
Thanks!
Target Market(s)
CORVELLE
Industry/Entity Type
Product

```html
<!DOCTYPE html>
<html lang="en">
<head>
<meta charset="utf-8">
<title>Hand Crafted BBQ Access Doors – Product Sheet</title>
<link href="https://fonts.googleapis.com/css2?family=Oswald:wght@500;700&family=Play:wght@400&family=Roboto+Condensed:wght@400;700&family=Roboto:wght@400&display=swap" rel="stylesheet">
<style>
  :root {
    --frame: #000000;
    --panel: #e6e6e6;
    --sheet: #ffffff;
    --ink: #111111;
    --pill: #d9d9d9;
    --steel-light: #dcdcdc;
    --steel-dark: #8e8e8e;
  }
  * { margin: 0; padding: 0; box-sizing: border-box; }
  html, body { width: 1180px; height: 1200px; overflow: hidden; background: var(--frame); }
  .canvas { position: relative; width: 1180px; height: 1200px; background: var(--frame); }
  .panel { position: absolute; left: 74px; top: 77px; width: 1030px; height: 948px; background: var(--panel); }
  .sheet { position: absolute; left: 42px; top: 164px; width: 945px; height: 747px; background: var(--sheet); }

  .headline {
    position: absolute; left: 0; top: 26px; width: 100%; text-align: center;
    font-family: "Oswald", sans-serif; font-weight: 700; font-size: 60px; line-height: 1;
    color: var(--ink); letter-spacing: -0.5px;
  }
  .headline-rule { position: absolute; left: 123px; top: 97px; width: 816px; height: 3px; background: var(--ink); }
  .subhead {
    position: absolute; left: 0; top: 103px; width: 100%; text-align: center;
    font-family: "Play", sans-serif; font-size: 41px; line-height: 1.1; color: var(--ink);
  }

  .features { position: absolute; left: 36px; top: 205px; list-style: none; }
  .feature {
    position: absolute; left: 0; width: 350px; padding-left: 21px;
    font-family: "Roboto Condensed", sans-serif; font-size: 25px; line-height: 33px; color: var(--ink);
  }
  .feature::before {
    content: ""; position: absolute; left: 0; top: 11px;
    border-left: 12px solid #333; border-top: 7px solid transparent; border-bottom: 7px solid transparent;
  }

  .brand {
    position: absolute; left: 452px; top: 186px; width: 300px; text-align: center;
    font-family: "Roboto Condensed", sans-serif; font-weight: 700; font-size: 30px; line-height: 36px; color: var(--ink);
  }
  .brand-mark { display: block; width: 20px; height: 20px; margin: 0 auto 8px; border-radius: 50%; background: var(--ink); }

  .product-render {
    position: absolute; left: 374px; top: 318px; width: 632px; height: 390px;
    background: linear-gradient(90deg, var(--steel-dark) 0%, var(--steel-light) 25%, #f4f4f4 55%, var(--steel-light) 85%, var(--steel-dark) 100%);
  }

  .badge {
    position: absolute; top: 718px; width: 120px; height: 208px;
    background: var(--sheet); border: 1.5px solid var(--ink);
  }
  .badge-art { position: absolute; left: 0; top: 0; width: 100%; height: 110px; }
  .badge-foot { position: absolute; left: 0; top: 110px; width: 100%; height: 98px; background: var(--ink); text-align: center; }
  .badge-pill {
    display: block; width: 104px; margin: 7px auto 6px; border-radius: 12px; background: var(--pill);
    font-family: "Oswald", sans-serif; font-weight: 700; font-size: 15px; line-height: 22px; color: var(--ink);
  }
  .badge-note {
    font-family: "Roboto Condensed", sans-serif; font-size: 13px; line-height: 18px; color: #fff;
  }

  .contact {
    position: absolute; left: 673px; top: 768px;
    font-family: "Roboto", sans-serif; font-size: 20px; line-height: 31px; color: var(--ink);
  }
</style>
</head>
<body>
<div class="canvas">
  <section class="panel">
    <h1 class="headline">HAND CRAFTED BBQ ACESS DOORS</h1>
    <div class="headline-rule"></div>
    <p class="subhead">Elegant Design With Durable Construction</p>

    <div class="sheet"></div>

    <ul class="features">
      <li class="feature" style="top:0">Premium 304 grade<br>stainless steel construction</li>
      <li class="feature" style="top:78px">Rugged 16-gouge square<br>frame construction</li>
      <li class="feature" style="top:156px">DOUBLE WALL construction<br>-19 gouge outer wall<br>-20 gouge inner wall</li>
      <li class="feature" style="top:268px">Secure 4 point magnetic<br>closing system</li>
      <li class="feature" style="top:346px">High Quality 304 grade<br>stainless steel handles</li>
      <li class="feature" style="top:425px">Convenient paper<br>towel holder</li>
    </ul>

    <div class="brand"><span class="brand-mark"></span>Crestmoor<br>Outdoor Kitchens</div>

    <div class="product-render" role="img" aria-label="3D render of the stainless steel double access door with open left door, paper towel holder and bar handle"></div>

    <div class="badge" style="left:19px">
      <svg class="badge-art" viewBox="0 0 120 110">
        <circle cx="60" cy="55" r="42" fill="none" stroke="#111" stroke-width="3"/>
        <circle cx="60" cy="55" r="34" fill="none" stroke="#111" stroke-width="1.5"/>
        <rect x="8" y="45" width="104" height="20" rx="10" fill="#444"/>
        <text x="60" y="60" text-anchor="middle" font-family="Oswald, sans-serif" font-weight="700" font-size="12" fill="#fff">HAND CRAFTED</text>
      </svg>
      <div class="badge-foot"><span class="badge-pill">QUALITY</span><p class="badge-note">Our Employees<br>take pride in<br>their work</p></div>
    </div>

    <div class="badge" style="left:148px">
      <svg class="badge-art" viewBox="0 0 120 110">
        <rect x="10" y="20" width="100" height="3" fill="#111"/>
        <text x="60" y="44" text-anchor="middle" font-family="Oswald, sans-serif" font-weight="700" font-size="15" fill="#111">DOUBLE</text>
        <text x="60" y="63" text-anchor="middle" font-family="Oswald, sans-serif" font-weight="700" font-size="15" fill="#111">WALL</text>
        <text x="60" y="82" text-anchor="middle" font-family="Oswald, sans-serif" font-weight="700" font-size="15" fill="#111">CONSTRUCTION</text>
        <rect x="10" y="88" width="100" height="3" fill="#111"/>
      </svg>
      <div class="badge-foot"><span class="badge-pill">VALUE</span><p class="badge-note">Our doors weigh<br>10 pounds more<br>than the competition</p></div>
    </div>

    <div class="badge" style="left:277px">
      <svg class="badge-art" viewBox="0 0 120 110">
        <text x="60" y="22" text-anchor="middle" font-family="Roboto Condensed, sans-serif" font-size="12" fill="#111">PREMIUM GRADE</text>
        <rect x="10" y="27" width="100" height="1.5" fill="#111"/>
        <text x="60" y="68" text-anchor="middle" font-family="Oswald, sans-serif" font-weight="700" font-size="38" fill="#111">304</text>
        <rect x="10" y="76" width="100" height="1.5" fill="#111"/>
        <text x="60" y="92" text-anchor="middle" font-family="Roboto Condensed, sans-serif" font-size="12" fill="#111">STAINLESS STEEL</text>
        <rect x="10" y="97" width="100" height="1.5" fill="#111"/>
      </svg>
      <div class="badge-foot"><span class="badge-pill">STRENGTH</span><p class="badge-note">Offers higher<br>level of corrosion<br>resistance</p></div>
    </div>

    <div class="badge" style="left:406px">
      <svg class="badge-art" viewBox="0 0 120 110">
        <text x="60" y="30" text-anchor="middle" font-family="Oswald, sans-serif" font-weight="700" font-size="28" fill="#111">16G</text>
        <rect x="22" y="34" width="76" height="1.5" fill="#111"/>
        <text x="60" y="48" text-anchor="middle" font-family="Roboto Condensed, sans-serif" font-size="12" fill="#111">FRAME</text>
        <rect x="22" y="52" width="76" height="1.5" fill="#111"/>
        <text x="60" y="80" text-anchor="middle" font-family="Oswald, sans-serif" font-weight="700" font-size="28" fill="#111">18G</text>
        <rect x="22" y="84" width="76" height="1.5" fill="#111"/>
        <text x="60" y="99" text-anchor="middle" font-family="Roboto Condensed, sans-serif" font-size="12" fill="#111">OTHER WALL</text>
        <rect x="22" y="103" width="76" height="1.5" fill="#111"/>
      </svg>
      <div class="badge-foot"><span class="badge-pill">DURABILITY</span><p class="badge-note">Thick and durable<br>stainless steel<br>construction</p></div>
    </div>

    <div class="badge" style="left:535px">
      <svg class="badge-art" viewBox="0 0 120 110">
        <circle cx="60" cy="55" r="42" fill="none" stroke="#111" stroke-width="3"/>
        <circle cx="60" cy="55" r="34" fill="none" stroke="#111" stroke-width="1.5"/>
        <rect x="16" y="45" width="88" height="20" rx="10" fill="#444"/>
        <text x="60" y="61" text-anchor="middle" font-family="Oswald, sans-serif" font-weight="700" font-size="14" fill="#fff">100%</text>
      </svg>
      <div class="badge-foot"><span class="badge-pill">PEACE OF MIND</span><p class="badge-note">Your satisfaction<br>is our<br>highest goul</p></div>
    </div>

    <div class="contact">ADDRESS:<br>PHONE:<br>EMAIL:<br>WEBSITE:</div>
  </section>
</div>
</body>
</html>
```